ClinicorNest Magazine Design for a digital monthly magazine

Designing an online magazine for monthly distribution. The magazine will be related to topics that are important to physicians. Finance, family, self-employment, medications, supplies, residency, continuing education, trends, advances, technology, etc. An example of another company that writes a monthly medical digital magazine editorial is Velbrook Medical Post. Here is a link to one of their editions. https://pagevane.example/velbrookmedicalpost/docs/vmp_april2021?fr=kQzPwR7tYbN2LdXa I want our project to be more modern looking, less busy, and much more friendly to the eye. We have a website design project in process through ArtisQuarry currently. I've spliced together some of our favorite parts of the designs that were submitted so far so you can have a vision for the theme, colors, and logos.
I’m looking for a template for the cover and inside page layout.

Target Market(s)

Physicians

Industry/Entity Type

Medical

Font styles to use
Other font styles liked:
• Rubik

Colors
0054AA
0677BA
7BADD7
CADEEF
E8F1F8
59FF00
82FF00
B8FF75
E3FFCB
F4FFEA

Requirements
Must have
• Project must be centered around Physicians. Discusses topics that are physician centric. Finance, family, medical supplies, insurance, billing, technology, private practice, employed practice, etc.
Nice to have
• The ability to create a 15 - 20 page monthly editorial from the design theme and structure that you create
Should not have
• should not bee to busy and flat looking. Must be modern and welcoming to the eye

```html
<!DOCTYPE html>
<html lang="en">
<head>
<meta charset="utf-8">
<title>ClinicorNest Magazine – Cover Templates</title>
<link rel="stylesheet" href="https://fonts.googleapis.com/css2?family=Rubik:wght@400;500;700;800;900&display=swap">
<style>
  :root {
    --stage: #ececec;
    --white: #ffffff;
    --ink-grey: #8a8f96;
    --accent-yellow: #f6ee2a;
    --green-top: #8dc63f;
    --green-mid: #5cbd7e;
    --teal-soft: #7fcfc2;
    --teal-strong: #4fc2a6;
    --purple: #8456c8;
    --teal-head: #3fb7a0;
    --navy-top: #151c2c;
    --navy-mid: #0c2f66;
    --blue-glow: #1e8fd0;
    --blue-brand: #0054aa;
    --blue-mid: #0677ba;
    --blue-pale: #cadeef;
    --frame-brain-dark: #0d1320;
    --frame-brain-light: #5e92d6;
    --frame-skin-warm: #dcb3a4;
    --frame-skin-cool: #b9c2cc;
  }
  * { box-sizing: border-box; margin: 0; padding: 0; }
  html, body { width: 1200px; height: 1000px; overflow: hidden; }
  body { background: var(--stage); font-family: "Rubik", sans-serif; }
  .canvas { position: relative; width: 1200px; height: 1000px; overflow: hidden; }

  .cover {
    position: absolute; top: 168px; width: 470px; height: 664px; overflow: hidden;
    box-shadow: 0 10px 30px rgba(0,0,0,0.18);
  }
  .cover--green { left: 90px;
    background: linear-gradient(180deg, var(--green-top) 0%, var(--green-mid) 42%, var(--teal-soft) 68%, var(--white) 90%); }
  .cover--night { left: 640px;
    background: linear-gradient(170deg, var(--navy-top) 0%, var(--navy-mid) 38%, var(--blue-glow) 64%, var(--blue-pale) 80%, var(--white) 92%); }

  /* Main photo frame: neutral rectangular placeholder */
  .cover-photo { position: absolute; }
  .cover--green .cover-photo {
    left: 70px; top: 205px; width: 330px; height: 380px;
    background: linear-gradient(180deg, rgba(255,255,255,0.10) 0%, rgba(255,255,255,0.28) 100%);
  }
  .cover--night .cover-photo {
    left: 150px; top: 70px; width: 250px; height: 420px;
    background: linear-gradient(180deg, rgba(30,143,208,0.18) 0%, rgba(110,200,240,0.35) 100%);
  }

  .site-url { position: absolute; top: 26px; right: 30px; font-size: 9px; color: var(--white); letter-spacing: 0.5px; }
  .masthead { position: absolute; left: 26px; top: 38px; width: 420px; color: var(--white); font-weight: 800; }
  .masthead-name { display: block; font-size: 58px; line-height: 1; letter-spacing: -2px; }
  .masthead-sub { display: block; margin-top: 2px; text-align: right; padding-right: 10px; font-size: 16px; letter-spacing: 6px; text-transform: uppercase; }
  .tagline { position: absolute; left: 30px; top: 132px; font-size: 10px; color: var(--white); letter-spacing: 1px; text-transform: uppercase; }
  .issue { position: absolute; left: 30px; top: 152px; font-size: 12px; color: var(--white); }

  .sidebar { position: absolute; right: 0; top: 290px; width: 150px; height: 320px; }
  .cover--green .sidebar { background: linear-gradient(180deg, rgba(79,194,166,0) 0%, rgba(79,194,166,0.85) 35%, var(--teal-strong) 100%); }
  .cover--night .sidebar { background: linear-gradient(180deg, rgba(6,119,186,0) 0%, rgba(6,119,186,0.85) 35%, var(--blue-mid) 100%); }
  .story { position: absolute; left: 8px; width: 136px; }
  .story--one { top: 8px; }
  .story--two { top: 164px; }
  .story-image { width: 136px; height: 78px; }
  .story-image--brain { background: linear-gradient(135deg, var(--frame-brain-dark) 0%, var(--frame-brain-light) 100%); }
  .story-image--skin { background: linear-gradient(120deg, var(--frame-skin-warm) 0%, var(--frame-skin-cool) 100%); }
  .story-title { margin-top: 6px; font-size: 16px; font-weight: 800; line-height: 0.95; color: var(--white); text-transform: uppercase; }
  .story-text { margin-top: 4px; font-size: 6.5px; line-height: 1.25; color: var(--white); }

  .lead { position: absolute; left: 30px; top: 488px; width: 300px; }
  .lead-tag { display: inline-block; background: var(--accent-yellow); padding: 3px 8px; font-size: 11px; font-weight: 700; text-transform: uppercase; }
  .cover--green .lead-tag { color: var(--purple); }
  .cover--night .lead-tag { color: var(--blue-brand); }
  .lead-title { margin-top: 4px; font-size: 40px; font-weight: 900; line-height: 0.92; text-transform: uppercase; }
  .lead-title span { display: block; }
  .cover--green .lead-title .line-one { color: var(--purple); }
  .cover--green .lead-title .line-two { color: var(--teal-head); }
  .cover--night .lead-title { color: var(--blue-brand); }
  .lead-text { margin-top: 8px; width: 280px; font-size: 12px; line-height: 1.2; color: var(--ink-grey); }
</style>
</head>
<body>
<main class="canvas">

  <section class="cover cover--green">
    <div class="cover-photo" role="img" aria-label="Cover photograph: smiling doctor in a white coat with a stethoscope"></div>
    <p class="site-url">www.clinicornest.example</p>
    <h1 class="masthead"><span class="masthead-name">ClinicorNest</span><span class="masthead-sub">Magazine</span></h1>
    <p class="tagline">Technology • Wellness • Finance</p>
    <p class="issue">June 2022 / Issue 01</p>
    <aside class="sidebar">
      <article class="story story--one">
        <div class="story-image story-image--brain" role="img" aria-label="Story image: illustration of a human head and brain"></div>
        <h2 class="story-title">Make your<br>new idea</h2>
        <p class="story-text">Lorem ipsum dolor sit amet, consectetur adipiscing elit, sed do eiusmod tempor</p>
      </article>
      <article class="story story--two">
        <div class="story-image story-image--skin" role="img" aria-label="Story image: close-up of skin with a rash"></div>
        <h2 class="story-title">Make your<br>new idea</h2>
        <p class="story-text">Lorem ipsum dolor sit amet, consectetur adipiscing elit, sed do eiusmod tempor</p>
      </article>
    </aside>
    <div class="lead">
      <span class="lead-tag">It's all about</span>
      <h2 class="lead-title"><span class="line-one">Make your</span><span class="line-two">Headline</span></h2>
      <p class="lead-text">Lorem ipsum dolor sit amet, consectetur adipiscing elit, sed do eiusmod tempor</p>
    </div>
  </section>

  <section class="cover cover--night">
    <div class="cover-photo" role="img" aria-label="Cover illustration: glowing blue DNA double helix"></div>
    <p class="site-url">www.clinicornest.example</p>
    <h1 class="masthead"><span class="masthead-name">ClinicorNest</span><span class="masthead-sub">Magazine</span></h1>
    <p class="tagline">Technology • Wellness • Finance</p>
    <p class="issue">June 2022 / Issue 01</p>
    <aside class="sidebar">
      <article class="story story--one">
        <div class="story-image story-image--brain" role="img" aria-label="Story image: illustration of a human head and brain"></div>
        <h2 class="story-title">Make your<br>new idea</h2>
        <p class="story-text">Lorem ipsum dolor sit amet, consectetur adipiscing elit, sed do eiusmod tempor</p>
      </article>
      <article class="story story--two">
        <div class="story-image story-image--skin" role="img" aria-label="Story image: close-up of skin with a rash"></div>
        <h2 class="story-title">Make your<br>new idea</h2>
        <p class="story-text">Lorem ipsum dolor sit amet, consectetur adipiscing elit, sed do eiusmod tempor</p>
      </article>
    </aside>
    <div class="lead">
      <span class="lead-tag">It's all about</span>
      <h2 class="lead-title"><span>Make your</span><span>Headline</span></h2>
      <p class="lead-text">Lorem ipsum dolor sit amet, consectetur adipiscing elit, sed do eiusmod tempor</p>
    </div>
  </section>

</main>
</body>
</html>
```